Drifting Past Solvane website

A very basic website using the graphics provided. The site would give the user the ability to read a description of the book, read testimonials, About the author, Read chapter 1, link to vendoro, order direct via coinlet.

```html
<!DOCTYPE html>
<html lang="en">
<head>
<meta charset="utf-8">
<title>Drifting Past Solvane</title>
<link rel="stylesheet" href="https://fonts.googleapis.com/css2?family=Cinzel:wght@700&family=Open+Sans:ital,wght@0,400;0,600;1,400&display=swap">
<style>
:root{
  --ink:#000;
  --paper:#efece4;
  --bar:#cdc5b8;
  --text:#6f6a62;
  --dark:#3b3833;
  --accent:#d97a10;
  --button:#f7a11a;
  --gold:#f2c33a;
  --rule:#c9c3b8;
  --frame:#e3dbd1;
  --star:#e8890c;
  --star-off:#8c8a86;
  --red:#b94141;
}
*{box-sizing:border-box;margin:0;padding:0}
html,body{width:1200px;height:800px;overflow:hidden}
body{position:relative;background:var(--paper);font-family:"Open Sans",sans-serif;color:var(--text)}
.abs{position:absolute}
.cover-side{left:0;top:0;width:585px;height:800px;background:var(--ink)}
.cover{left:115px;top:69px;width:426px;height:654px;overflow:hidden}
.cover-band{left:0;top:0;width:100%;height:150px;background:radial-gradient(ellipse at 50% 55%,#8a2a12 0%,#5a160c 60%,#2d0a06 100%)}
.cover-art{left:0;top:148px;width:100%;height:506px;background:linear-gradient(180deg,#5a6b6a 0%,#7fa0a8 25%,#5b6a48 50%,#3a2a18 75%,#120d08 100%)}
.cover-title{width:100%;text-align:center;font-family:"Cinzel",serif;color:var(--gold);text-shadow:0 2px 3px #000}
.t1{top:40px;font-size:34px;letter-spacing:1px}
.t2{top:88px;font-size:40px}
.cover-author{top:575px;width:100%;text-align:center;font-family:"Cinzel",serif;font-size:33px;color:#d9cfb2;text-shadow:0 2px 3px #000}
.topbar{left:585px;top:0;width:615px;height:57px;background:var(--bar);border-bottom:1px solid #b7ae9f;z-index:2}
.shop{top:1px;width:67px;height:55px;background:#f7f6f2;text-align:center}
.shop-label{height:17px;font-size:9px;line-height:17px;color:#fff}
.shop-name{font-size:14px;font-weight:600;line-height:36px;color:var(--dark)}
.coinlet{left:335px}.coinlet .shop-label{background:var(--red)}
.vendoro{left:403px}.vendoro .shop-label{background:var(--button)}
.photo-frame{left:626px;top:40px;width:173px;height:55px;background:var(--frame);padding:0 8px 8px}
.photo{width:100%;height:100%;background:linear-gradient(90deg,#3a3531,#8a766a 50%,#1e1c1b)}
.copy{font-size:11.2px;line-height:16.3px;letter-spacing:.3px}
.rule{height:1px;background:var(--rule);left:694px;width:329px}
.book-frame{left:626px;top:178px;width:173px;height:173px;background:var(--frame);padding:8px}
.book{width:100%;height:100%;background:radial-gradient(ellipse at 45% 50%,#3d3a30 0%,#201d18 45%,#f6f4ef 70%)}
.heading{font-family:"Cinzel",serif;font-size:16px;color:var(--accent);letter-spacing:.5px}
.read-btn{left:811px;top:381px;width:128px;height:38px;background:var(--button);border-radius:3px;color:#fff;font-size:14px;font-weight:600;line-height:38px;text-align:center;letter-spacing:.5px;box-shadow:0 1px 1px #b8730d}
.review{left:626px;width:455px}
.reviewer{font-size:12px;letter-spacing:.4px;color:var(--dark);display:flex;align-items:center;gap:5px}
.stars{display:flex;gap:3px}
.quote{font-size:11px;font-style:italic;line-height:16.3px;letter-spacing:.5px;margin-top:2px}
.quote::before{content:"\201C";font-style:normal;font-weight:600;color:#a9a59c;font-size:15px;margin-right:4px;vertical-align:-2px}
.track{left:1095px;top:118px;width:4px;height:653px;background:#dcd7cf;border-radius:2px}
.thumb{left:1095px;top:501px;width:4px;height:270px;background:#8e8a84;border-radius:2px}
.to-top{left:1125px;top:716px;width:34px;height:34px;border-radius:50%;background:#3d3b39}
</style>
</head>
<body>
<section class="abs cover-side">
  <div class="abs cover">
    <div class="abs cover-band" role="img" aria-label="Deep red damask pattern behind the title"></div>
    <div class="abs cover-art" role="img" aria-label="Silhouette of a man behind prison bars looking out to a palm-lined tropical beach"></div>
    <div class="abs cover-title t1">Drifting Past</div>
    <div class="abs cover-title t2">Solvane</div>
    <div class="abs cover-author">Jonah Arlen</div>
  </div>
</section>

<header class="abs topbar">
  <a class="abs shop coinlet"><div class="shop-label">Buy Now</div><div class="shop-name">coinlet</div></a>
  <a class="abs shop vendoro"><div class="shop-label">Order Now</div><div class="shop-name">vendoro</div></a>
</header>

<div class="abs photo-frame"><div class="photo" role="img" aria-label="Portrait of the author"></div></div>
<p class="abs copy" style="left:811px;top:53px;width:270px">debitis aut rerum necessitatibus saepe eveniet ut et voluptates repudiandae sint et molestiae non recusandae.</p>
<div class="abs rule" style="top:146px"></div>

<div class="abs book-frame"><div class="book" role="img" aria-label="3D view of the book Drifting Past Solvane"></div></div>
<h2 class="abs heading" style="left:811px;top:193px">DESCRIPTION OF THE BOOK</h2>
<p class="abs copy" style="left:811px;top:228px;width:275px">Nemo enim ipsam voluptatem quia voluptas sit aspernatur aut odit aut fugit, sed quia conse-quuntur magni dolores eos qui ratione volupta-tem sequi nesciunt. Neque porro quisquam est, qui dolorem ipsum quia dolor sit amet, con-sectetur, adipisci velit, sed quia non numquam eius modi tempora incidunt ut labore et dolore magnam aliquam quaerat voluptatem.</p>
<a class="abs read-btn">Read chapter 1</a>
<div class="abs rule" style="top:443px"></div>

<h2 class="abs heading" style="left:626px;top:490px">TESTIMONIALS</h2>
<svg width="0" height="0" style="position:absolute"><defs><path id="star" d="M5 0l1.5 3.3 3.5.4-2.6 2.4.7 3.5L5 7.8 1.9 9.6l.7-3.5L0 3.7l3.5-.4z"/></defs></svg>

<div class="abs review" style="top:519px">
  <div class="reviewer">Owen Hale rated it <span class="stars"><svg width="10" height="10"><use href="#star" fill="var(--star)"/></svg><svg width="10" height="10"><use href="#star" fill="var(--star)"/></svg><svg width="10" height="10"><use href="#star" fill="var(--star)"/></svg><svg width="10" height="10"><use href="#star" fill="var(--star-off)"/></svg></span></div>
  <p class="quote">Quis autem vel eum iure reprehenderit qui in ea voluptate velit esse quam.</p>
</div>
<div class="abs review" style="top:558px">
  <div class="reviewer">Luke Marsh rated it <span class="stars"><svg width="10" height="10"><use href="#star" fill="var(--star)"/></svg><svg width="10" height="10"><use href="#star" fill="var(--star)"/></svg><svg width="10" height="10"><use href="#star" fill="var(--star)"/></svg><svg width="10" height="10"><use href="#star" fill="var(--star)"/></svg></span></div>
  <p class="quote" style="margin-top:5px">Consequatur, vel illum qui dolorem eum fugiat quo voluptas nulla pariatur.voluptatibus.</p>
</div>
<div class="abs review" style="top:619px">
  <div class="reviewer">Mr.Tobin rated it <span class="stars"><svg width="10" height="10"><use href="#star" fill="var(--star)"/></svg><svg width="10" height="10"><use href="#star" fill="var(--star)"/></svg><svg width="10" height="10"><use href="#star" fill="var(--star)"/></svg><svg width="10" height="10"><use href="#star" fill="var(--star-off)"/></svg></span></div>
  <p class="quote" style="margin-top:5px">Itaque earum rerum hic tenetur a sapiente delectus, ut aut reiciendis voluptatibus maiores.</p>
</div>
<div class="abs review" style="top:678px">
  <div class="reviewer">Mr.Elric rated it <span class="stars"><svg width="10" height="10"><use href="#star" fill="var(--star)"/></svg><svg width="10" height="10"><use href="#star" fill="var(--star)"/></svg><svg width="10" height="10"><use href="#star" fill="var(--star)"/></svg><svg width="10" height="10"><use href="#star" fill="var(--star)"/></svg></span></div>
  <p class="quote" style="margin-top:6px">Neque porro quisquam est, qui dolorem ipsum quia dolor sit amet consectetur.</p>
</div>

<div class="abs track"></div>
<div class="abs thumb"></div>
<a class="abs to-top"><svg width="34" height="34" viewBox="0 0 34 34"><path d="M11 20l6-6 6 6" fill="none" stroke="#fff" stroke-width="2.6" stroke-linecap="round" stroke-linejoin="round"/></svg></a>
</body>
</html>
```